Real Estate Brokerage Informational Handbill

A 4 X 6 handbill to promote a real estate brokerage modeled after the design attached including attached logo and information.
These handbills should provide a high-level overview of what we do at the brokerage and should be attractive and be inviting.
The goal of the handbill is to have motivated clients in the market to buy or sell their home or property call or visit our website

Target Market(s)

Buyers and sellers of real estate in the Rochester NY area ages 24 - 60

Industry/Entity Type

Real Estate

Font styles to use
Sans Serif

Requirements
Must have
• Please include all the information contained on current handbill
• remove the line "we will walk you through the home buying process at no cost to you".
• replace with "come to one of our monthly first-time buyer informational sessions".
• add the phrase "have your reviewed and receive customized Home Purchase Plan"
• Add the slogan "Bright Path Realty Helping Motivated People Achieve Their Real Estate Goals"
Nice to have
• 2 sided design

```html
<!DOCTYPE html>
<html lang="en">
<head>
<meta charset="utf-8">
<title>Bright Path Realty Handbill</title>
<link rel="stylesheet" href="https://fonts.googleapis.com/css2?family=Cabin:wght@400;600;700&family=Archivo+Black&family=Cinzel:wght@400;600&display=swap">
<style>
  :root {
    --backdrop: #222222;
    --paper: #ffffff;
    --mist: #e6e6e8;
    --mist-dark: #c9c9cc;
    --rose: #ee6479;
    --rose-deep: #d94d64;
    --sun: #fdc72f;
    --ink: #2b2b2b;
    --slate: #3a3d45;
  }
  * { margin: 0; padding: 0; box-sizing: border-box; }
  html, body {
    width: 928px; height: 1200px; overflow: hidden;
    background: var(--backdrop);
    font-family: "Cabin", sans-serif;
  }
  .card {
    position: absolute; left: 137px; width: 654px; height: 435px;
    overflow: hidden;
  }
  .card--front { top: 159px; background: var(--mist); }
  .card--back { top: 606px; background: var(--paper); }

  .front-shapes { position: absolute; inset: 0; }
  .headline {
    position: absolute; top: 12px; left: 0; width: 654px;
    text-align: center; color: var(--ink);
    font-size: 27px; line-height: 33px;
  }
  .headline strong { font-weight: 700; }
  .session-band {
    position: absolute; top: 125px; left: 0; width: 610px; height: 26px;
    background: var(--sun); border-radius: 0 13px 13px 0;
    font-weight: 700; font-size: 17px; line-height: 26px;
    color: var(--ink); padding-left: 41px;
  }
  .plan-question {
    position: absolute; top: 157px; left: 43px;
    font-size: 25px; line-height: 29px; color: var(--ink);
  }
  .handshake-photo { position: absolute; left: 433px; top: 222px; width: 221px; height: 140px; }
  .services {
    position: absolute; top: 268px; left: 47px; list-style: none;
  }
  .services .lead {
    font-size: 16px; color: var(--ink); line-height: 22px; margin-bottom: 2px;
  }
  .services .item {
    font-weight: 700; font-size: 19px; color: #fff; line-height: 24px;
    position: relative; padding-left: 9px; margin-left: -10px;
  }
  .services .item::before {
    content: ""; position: absolute; left: 0; top: 10px;
    width: 5px; height: 5px; border-radius: 50%; background: var(--sun);
  }
  .brand-badge {
    position: absolute; left: 470px; top: 200px; width: 126px; height: 58px;
    border-radius: 50%; background: var(--mist);
    display: flex; align-items: center; justify-content: center;
    text-align: center; font-weight: 700; font-size: 15px; line-height: 17px;
    color: var(--slate);
  }
  .sell-note {
    position: absolute; top: 372px; width: 100%; text-align: center;
    font-size: 17px; color: var(--ink);
  }
  .call-line {
    position: absolute; top: 390px; width: 100%; text-align: center;
    font-family: "Archivo Black", sans-serif; font-size: 36px;
    letter-spacing: 1px; color: var(--ink);
  }

  .desk-photo { position: absolute; left: 0; top: 0; width: 654px; height: 280px; }
  .slogan {
    position: absolute; top: 274px; left: 29px;
    font-family: "Cinzel", serif; font-size: 27px; line-height: 33px;
    color: var(--slate); font-variant: small-caps; letter-spacing: 1px;
  }
  .brand-mark {
    position: absolute; left: 425px; top: 280px; width: 177px; height: 96px;
    display: flex; align-items: center; justify-content: center; gap: 10px;
    font-family: "Cinzel", serif; font-weight: 600; font-size: 19px; line-height: 22px;
    color: var(--slate); text-align: center;
  }
  .brand-mark .dot { width: 14px; height: 14px; border-radius: 50%; background: var(--rose); flex: none; }
  .stripe { position: absolute; left: 0; }
  .stripe--rose { top: 384px; width: 574px; height: 13px; background: var(--rose); }
  .stripe--sun { top: 398px; width: 556px; height: 8px; background: var(--sun); }
</style>
</head>
<body>

<section class="card card--front">
  <svg class="front-shapes" width="654" height="435" viewBox="0 0 654 435">
    <polygon points="0,261 654,184 654,218 0,270" fill="var(--mist-dark)"/>
    <polygon points="0,270 654,218 654,435 0,435" fill="var(--rose)"/>
    <rect x="0" y="363" width="654" height="3" fill="var(--sun)"/>
  </svg>

  <svg class="handshake-photo" role="img" aria-label="Photo of a handshake in front of a house" viewBox="0 0 221 140" preserveAspectRatio="none">
    <defs>
      <linearGradient id="handshakeFade" x1="0" x2="1" y1="0" y2="0">
        <stop offset="0" stop-color="#ee6479" stop-opacity="0"/>
        <stop offset="0.5" stop-color="#d98a94" stop-opacity="0.7"/>
        <stop offset="1" stop-color="#e7b5bb"/>
      </linearGradient>
    </defs>
    <rect width="221" height="140" fill="url(#handshakeFade)"/>
  </svg>

  <h1 class="headline">First Time Home Buyer's Specialists<br>Assisting you with all of your real estate<br>needs from <strong>CREDIT</strong> to <strong>CLOSING</strong> and beyond</h1>
  <p class="session-band">Come to one of our monthly first-time buyer informational sessions</p>
  <p class="plan-question">Have your credit reviewed and receive personalized<br>Home Purchase Plan?</p>

  <div class="brand-badge">Bright Path<br>Realty</div>

  <ul class="services">
    <li class="lead">First Time Buyer Grant Assistance Credit Counseling</li>
    <li class="item">Rochester's Best Realtors</li>
    <li class="item">Customized Property Search</li>
    <li class="item">Closing and Post-Closing Assistance</li>
  </ul>

  <p class="sell-note">Need to Sell your property Call us today for a free consultation</p>
  <p class="call-line">Call Us Today at 555-HOME</p>
</section>

<section class="card card--back">
  <svg class="desk-photo" role="img" aria-label="Photo of a model house beside hands signing a contract with house keys" viewBox="0 0 654 280" preserveAspectRatio="none">
    <defs>
      <linearGradient id="deskFade" x1="0" x2="1" y1="0" y2="1">
        <stop offset="0" stop-color="#f3f3f4"/>
        <stop offset="0.55" stop-color="#e4e4e6"/>
        <stop offset="1" stop-color="#ffffff"/>
      </linearGradient>
    </defs>
    <rect width="654" height="280" fill="url(#deskFade)"/>
  </svg>

  <p class="slogan">Helping Motivated People<br>Achieve Their<br>Real Estate Goals</p>
  <div class="brand-mark"><span class="dot"></span><span>Bright Path<br>Realty</span></div>

  <div class="stripe stripe--rose"></div>
  <div class="stripe stripe--sun"></div>
</section>

</body>
</html>
```